We are an education and business training and consulting company focused on helping companies maximize their growth potential. Our goal is provide targeted human resource solutions to organizational problems.
Target Market(s)
School districts and businesses of all types
Industry/Entity Type
Education
Contact Information for Business Card
Brightpath Learning Partners LLC
Leonard Kimble president
Business and Education Training and Consulting
517 Cedar Brook Lane
Naples, Florida 34689
(239) 457-3196
Leonard.kimble@brightpathlearningpartners.com
Font styles to use
Colors
Designer to choose colors to be used in the design.
Look and feel
Each slider illustrates characteristics of the customer's brand and the style your logo design should communicate.

```html
<!DOCTYPE html>
<html lang="en">
<head>
<meta charset="utf-8">
<title>Brightpath Learning Partners – Business Card</title>
<link rel="stylesheet" href="https://fonts.googleapis.com/css2?family=Exo+2:wght@400;500;600&display=swap">
<style>
  :root {
    --brand-blue: #3d3f96;
    --card-white: #f4f4f4;
    --card-grey: #d9d9d9;
    --ink: #2e2e33;
    --on-blue: #ffffff;
    --backdrop: #e8e6e1;
  }
  * { margin: 0; padding: 0; box-sizing: border-box; }
  html, body {
    width: 1200px;
    height: 1085px;
    overflow: hidden;
    background: var(--backdrop);
    font-family: "Exo 2", "Helvetica Neue", Arial, sans-serif;
  }
  .card {
    position: absolute;
    left: 160px;
    width: 880px;
    height: 503px;
    overflow: hidden;
    box-shadow: 0 6px 18px rgba(0,0,0,0.18);
  }
  .card--front { top: 20px; background: var(--brand-blue); color: var(--on-blue); }
  .card--back { top: 563px; background: var(--brand-blue); }

  .front__company {
    position: absolute;
    left: 300px;
    top: 150px;
    font-size: 17px;
    letter-spacing: 0.5px;
  }
  .front__name {
    position: absolute;
    left: 300px;
    top: 265px;
    font-size: 44px;
    font-weight: 500;
    letter-spacing: 2px;
    text-transform: uppercase;
    line-height: 1;
  }
  .front__title {
    position: absolute;
    left: 330px;
    top: 318px;
    font-size: 32px;
    font-weight: 400;
    line-height: 1;
  }

  .back__panel { position: absolute; left: 0; top: 0; width: 880px; height: 503px; }
  .back__icon { position: absolute; width: 64px; height: 64px; }
  .contact {
    position: absolute;
    right: 330px;
    text-align: right;
    color: var(--ink);
    font-size: 24px;
    line-height: 1.3;
    letter-spacing: 0.5px;
  }
  .contact--phone { top: 88px; }
  .contact--address { top: 192px; }
  .contact--web { top: 340px; font-size: 20px; }
</style>
</head>
<body>

<section class="card card--front" aria-label="Business card front">
  <p class="front__company">Brightpath Learning Partners LLC</p>
  <h1 class="front__name">Leonard Kimble</h1>
  <p class="front__title">President</p>
</section>

<section class="card card--back" aria-label="Business card back">
  <svg class="back__panel" viewBox="0 0 880 503" aria-hidden="true">
    <defs>
      <linearGradient id="panelShade" x1="0" y1="0" x2="1" y2="1">
        <stop offset="0" stop-color="#c9c9c9"/>
        <stop offset="0.45" stop-color="var(--card-white)"/>
        <stop offset="1" stop-color="#dcdcdc"/>
      </linearGradient>
    </defs>
    <path fill="url(#panelShade)"
      d="M0 0 H600 V72 A46 46 0 0 1 600 164 V194 A46 46 0 0 1 600 286 V318 A46 46 0 0 1 600 410 V503 H0 Z"/>
  </svg>

  <svg class="back__icon" style="left:568px;top:86px" viewBox="0 0 64 64" aria-label="Phone">
    <circle cx="32" cy="32" r="28" fill="none" stroke="var(--brand-blue)" stroke-width="3"/>
    <path d="M22 20 q-4 3 -1 10 q6 12 16 15 q6 2 8 -2 l-5 -5 q-3 2 -5 1 q-5 -3 -8 -9 q-1 -2 1 -4 Z" fill="var(--brand-blue)"/>
  </svg>
  <svg class="back__icon" style="left:568px;top:208px" viewBox="0 0 64 64" aria-label="Location">
    <circle cx="32" cy="32" r="28" fill="var(--brand-blue)"/>
    <path d="M32 16 a10 10 0 0 1 10 10 c0 8 -10 20 -10 20 s-10 -12 -10 -20 a10 10 0 0 1 10 -10 Z" fill="var(--card-white)"/>
    <circle cx="32" cy="26" r="4" fill="var(--brand-blue)"/>
  </svg>
  <svg class="back__icon" style="left:568px;top:332px" viewBox="0 0 64 64" aria-label="Web">
    <circle cx="32" cy="32" r="28" fill="none" stroke="var(--brand-blue)" stroke-width="3"/>
    <g fill="none" stroke="var(--brand-blue)" stroke-width="2.5">
      <circle cx="32" cy="32" r="15"/>
      <ellipse cx="32" cy="32" rx="6" ry="15"/>
      <line x1="17" y1="32" x2="47" y2="32"/>
      <line x1="19" y1="24" x2="45" y2="24"/>
      <line x1="19" y1="40" x2="45" y2="40"/>
    </g>
  </svg>

  <p class="contact contact--phone">(239) 457-3196</p>
  <p class="contact contact--address">517 Cedar Brook Lane,<br>Naples, Florida<br>34689</p>
  <p class="contact contact--web">Leonard.kimble@brightpathlearningpartners.com<br>brightpathlearningpartners.com</p>
</section>

</body>
</html>
```